Long Established Local Fencing (not swords) Business needs fresh Business Cards

We need fresh double sided business cards for our Fencing Construction business, we are looking for something with our new logo design added, and maybe a photo background ?
We recently had cards made from Cardlyne and we were horrified with what we got back, the quality was terrible, so am looking for high quality format for good printing company to make.
We install Steelmora, Timber paling, Aluminium Slat Screening, Picket (timber and aluminium) and most other fencing installations.
Our website is brankelrails.com.au should you like to learn a bit more.
We do have logo in other formats if required.
We have been in business for over 35 years and we have used this as a "motto" it is on our signage

Industry/Entity Type

Construction

Contact Information for Business Card

Open to ideas, we need 3 x different cards, one generic with no name and 2 x others each with 1 of our bosses name on each, I will put into upload files.

Colors
ec1f27
000000
606060
f5f5f5

Requirements
Must have
• Company Name and Logo
• Address
• Contact details, phone, website, email etc
• Small space to write notes when leaving card at residence
Nice to have
• Our motto "Servicing the Peninsula for over 35 years"

```html
<!DOCTYPE html>
<html lang="en">
<head>
<meta charset="utf-8">
<title>Brankel Rails – Business Cards</title>
<link rel="stylesheet" href="https://fonts.googleapis.com/css2?family=Michroma&family=Bebas+Neue&family=Arimo:wght@400&display=swap">
<style>
  :root {
    --red: #d1262b;
    --black: #151515;
    --grey: #606060;
    --card: #e6e6e6;
    --stage: #d6d6d6;
    --text-light: #f5f5f5;
    --body-grey: #4a4a4a;
  }
  * { margin: 0; padding: 0; box-sizing: border-box; }
  html, body { width: 1200px; height: 1200px; overflow: hidden; }
  body {
    background: var(--stage);
    position: relative;
    font-family: "Arimo", Arial, sans-serif;
  }
  .brand-lockup {
    position: absolute; left: 48px; top: 100px;
    display: flex; align-items: center; gap: 28px;
  }
  .brand-dot {
    width: 150px; height: 150px; border-radius: 50%;
    background: var(--black);
  }
  .wordmark {
    font-family: "Michroma", sans-serif;
    color: var(--black);
    line-height: 1.05;
    text-transform: uppercase;
  }
  .brand-lockup .wordmark { font-size: 52px; }
  .variant-label {
    position: absolute; left: 704px; top: 128px;
    font-family: "Bebas Neue", sans-serif;
    font-size: 92px; line-height: 1;
    color: var(--black);
    letter-spacing: -1px;
  }
  .card {
    position: absolute; width: 520px; height: 296px;
    background: var(--card);
    box-shadow: 0 2px 3px rgba(0,0,0,0.35);
    overflow: hidden;
  }
  .card--mark { left: 60px; top: 398px; }
  .card--dale { left: 620px; top: 398px; }
  .card--general { left: 60px; top: 803px; }
  .card--notes { left: 620px; top: 803px; }
  .card .wordmark {
    position: absolute; left: 24px; top: 20px;
    font-size: 31px;
  }
  .band {
    position: absolute; left: 0; width: 520px;
    background: var(--black);
  }
  .band__accent {
    position: absolute; right: 0; top: 0; bottom: 0; width: 70px;
    background: var(--red);
  }
  .band__disc {
    position: absolute; right: 60px; top: 50%;
    width: 120px; height: 120px; margin-top: -60px; border-radius: 50%;
    background: var(--grey);
  }
  .card--mark .band, .card--dale .band { top: 117px; height: 123px; }
  .card--general .band { top: 125px; height: 118px; }
  .person {
    position: absolute; left: 24px; top: 10px;
    color: var(--red); font-size: 17px; text-transform: uppercase;
  }
  .contacts {
    position: absolute; left: 24px; list-style: none;
    color: var(--text-light); font-size: 13px; line-height: 17.5px;
  }
  .card--mark .contacts, .card--dale .contacts { top: 44px; }
  .card--general .contacts { top: 54px; }
  .contacts li { display: flex; align-items: center; gap: 8px; }
  .contacts svg { width: 11px; height: 11px; flex: none; }
  .band-address {
    position: absolute; left: 24px; top: 10px;
    color: var(--text-light); font-size: 13px; line-height: 17.5px;
  }
  .address {
    position: absolute; left: 22px; top: 258px;
    color: var(--body-grey); font-size: 13px;
  }
  .notes-head {
    position: absolute; left: 225px; top: 48px;
  }
  .notes-head .wordmark { position: static; font-size: 31px; }
  .notes-dot {
    position: absolute; left: 110px; top: 44px;
    width: 96px; height: 96px; border-radius: 50%; background: var(--black);
  }
  .license {
    margin-top: 8px; font-size: 13.5px; letter-spacing: 4px; color: var(--black);
  }
  .license span { color: var(--red); }
  .write-line {
    position: absolute; left: 16px; width: 490px; height: 1px;
    background: var(--grey);
  }
  .footer-rule {
    position: absolute; left: 0; right: 0; top: 256px; height: 3px; background: var(--red);
  }
  .footer-band {
    position: absolute; left: 0; right: 0; top: 259px; bottom: 0;
    background: var(--black);
    color: var(--text-light); font-size: 13px; letter-spacing: 2.5px;
    display: flex; align-items: center; justify-content: center;
  }
  .footer-band span { color: var(--red); margin-right: 8px; }
</style>
</head>
<body>
  <svg width="0" height="0" style="position:absolute" aria-hidden="true">
    <defs>
      <symbol id="ico-phone" viewBox="0 0 12 12"><circle cx="6" cy="6" r="6" fill="#d1262b"/><path d="M3.6 3.2l1.2-.4.8 1.6-.7.6c.4.9 1 1.5 1.9 1.9l.6-.7 1.6.8-.4 1.2c-2.6-.2-4.8-2.4-5-5z" fill="#151515"/></symbol>
      <symbol id="ico-mobile" viewBox="0 0 12 12"><circle cx="6" cy="6" r="6" fill="#d1262b"/><rect x="4" y="2.6" width="4" height="6.8" rx=".7" fill="#151515"/></symbol>
      <symbol id="ico-mail" viewBox="0 0 12 12"><circle cx="6" cy="6" r="6" fill="#d1262b"/><rect x="3" y="4" width="6" height="4.2" fill="none" stroke="#151515" stroke-width=".9"/><path d="M3 4l3 2.4L9 4" fill="none" stroke="#151515" stroke-width=".9"/></symbol>
      <symbol id="ico-web" viewBox="0 0 12 12"><circle cx="6" cy="6" r="6" fill="#d1262b"/><circle cx="6" cy="6" r="3.2" fill="none" stroke="#151515" stroke-width=".8"/><path d="M2.8 6h6.4M6 2.8c-1.6 2-1.6 4.4 0 6.4M6 2.8c1.6 2 1.6 4.4 0 6.4" fill="none" stroke="#151515" stroke-width=".7"/></symbol>
    </defs>
  </svg>

  <header class="brand-lockup">
    <div class="brand-dot"></div>
    <div class="wordmark">Brankel<br>Rails</div>
  </header>
  <div class="variant-label">WITHOUT SLOGON</div>

  <section class="card card--mark">
    <div class="wordmark">Brankel<br>Rails</div>
    <div class="band">
      <div class="band__accent"></div>
      <div class="band__disc"></div>
      <div class="person">Tom Keller</div>
      <ul class="contacts">
        <li><svg><use href="#ico-phone"/></svg>(02) 4390 1287</li>
        <li><svg><use href="#ico-mobile"/></svg>0400 555 218</li>
        <li><svg><use href="#ico-mail"/></svg>brankelrails@netmail.com</li>
        <li><svg><use href="#ico-web"/></svg>www.brankelrails.com.au</li>
      </ul>
    </div>
    <div class="address">42 Harbour Rd, Kelton, NSW, 2000</div>
  </section>

  <section class="card card--dale">
    <div class="wordmark">Brankel<br>Rails</div>
    <div class="band">
      <div class="band__accent"></div>
      <div class="band__disc"></div>
      <div class="person">Dale Morrow</div>
      <ul class="contacts">
        <li><svg><use href="#ico-phone"/></svg>(02) 4390 1287</li>
        <li><svg><use href="#ico-mobile"/></svg>0400 555 734</li>
        <li><svg><use href="#ico-mail"/></svg>brankelrails@netmail.com</li>
        <li><svg><use href="#ico-web"/></svg>www.brankelrails.com.au</li>
      </ul>
    </div>
    <div class="address">42 Harbour Rd, Kelton, NSW, 2000</div>
  </section>

  <section class="card card--general">
    <div class="wordmark">Brankel<br>Rails</div>
    <div class="band">
      <div class="band__accent"></div>
      <div class="band__disc"></div>
      <div class="band-address">42 Harbour Rd, Kelton,<br>NSW, 2000</div>
      <ul class="contacts">
        <li><svg><use href="#ico-phone"/></svg>(02) 4390 1287</li>
        <li><svg><use href="#ico-mail"/></svg>brankelrails@netmail.com</li>
        <li><svg><use href="#ico-web"/></svg>www.brankelrails.com.au</li>
      </ul>
    </div>
  </section>

  <section class="card card--notes">
    <div class="notes-dot"></div>
    <div class="notes-head">
      <div class="wordmark">Brankel<br>Rails</div>
      <div class="license"><span>License No.</span> 50214k</div>
    </div>
    <div class="write-line" style="top:175px"></div>
    <div class="write-line" style="top:205px"></div>
    <div class="write-line" style="top:234px"></div>
    <div class="footer-rule"></div>
    <div class="footer-band"><span>ABN</span>61402883175</div>
  </section>
</body>
</html>
```